Postcard Mailer to upscale luxury homeowners

We are a new company in the Tucson AZ market and want to use postcard marketing in key target markets. We clean and seal natural stone - granite, travertine, slate, etc. See website - http://www.brightharborstone.example/ for more information about about our services and before/after photos in our "gallery" section.The logo from the site - Bright Harbor Co - needs to be on the post card. The before/after photos from the photo "gallery" on the site demonstrate what can be done. We think a promo of $XXX off to any one requesting an estimate and presenting the postcard is worth trying. We have additional photos and information if needed.

Target Market(s)

Upscale residential homes in luxury home subdivisions

Industry/Entity Type

Home Improvement

Font styles to use
Sans Serif
Script

Requirements
Must have
• Logo
• Before/After photo (see website gallery for potential photos)
• website
• contact
• life time guarantee
• Feel of richness
Nice to have
• A call to action. $XXX dollar discount when estimate scheduled within/by ZZ
Should not have
• Won't know until I see it

```html
<!DOCTYPE html>
<html lang="en">
<head>
<meta charset="utf-8">
<title>Bright Harbor Co — Stone Sealing Postcard</title>
<link rel="stylesheet" href="https://fonts.googleapis.com/css2?family=Oswald:wght@500&family=Lora:ital,wght@0,400;0,700;1,400&family=Montserrat:wght@500;700&display=swap">
<style>
  :root {
    --navy: #0b4d7e;
    --navy-deep: #073a63;
    --ink: #1d1d1d;
    --accent: #1f6fae;
    --white: #ffffff;
    --paper-top: #d4e6f2;
    --paper-bottom: #f3f8fb;
    --rule: #8a9aa6;
  }
  * { box-sizing: border-box; margin: 0; padding: 0; }
  html, body { width: 933px; height: 1200px; overflow: hidden; background: #ffffff; }
  .canvas { position: relative; width: 933px; height: 1200px; }

  .card { position: absolute; left: 32px; width: 870px; overflow: hidden; }
  .card--front { top: 32px; height: 560px; background: var(--navy); }
  .card--back { top: 610px; height: 564px; background: linear-gradient(180deg, var(--paper-top) 0%, var(--paper-bottom) 70%); }

  .kitchen-photo { position: absolute; inset: 0 0 150px 0;
    background: linear-gradient(180deg, #6b3b24 0%, #8a5a3a 35%, #b08a6a 55%, #5e4636 100%); }
  .wave { position: absolute; left: 0; top: 300px; width: 870px; height: 260px; }

  .featured { position: absolute; right: 26px; top: 28px; display: flex; align-items: center; gap: 12px;
    color: var(--white); font-family: "Montserrat", sans-serif; }
  .featured__label { font-size: 16px; font-weight: 500; letter-spacing: 0.5px; }
  .featured__name { font-size: 26px; font-weight: 700; }

  .front-contact { position: absolute; right: 22px; top: 370px; text-align: right; color: var(--white); }
  .front-contact__phone { font-family: "Oswald", sans-serif; font-size: 34px; line-height: 1.1; }
  .front-contact__web { font-family: "Oswald", sans-serif; font-size: 26px; line-height: 1.3; }
  .front-contact__web span { color: #9fd2f4; }
  .front-contact__headline { font-family: "Oswald", sans-serif; font-size: 28px; margin-top: 14px; }
  .front-contact__tagline { font-family: "Lora", serif; font-style: italic; font-size: 19px; margin-top: 2px; }

  .brand-seal { position: absolute; display: flex; align-items: center; justify-content: center;
    border-radius: 50%; background: var(--white); border: 6px solid var(--navy-deep); text-align: center;
    font-family: "Lora", serif; font-weight: 700; color: var(--navy); }
  .brand-seal--front { left: 36px; top: 310px; width: 228px; height: 228px; font-size: 28px; line-height: 1.15; }
  .brand-seal--back { left: 26px; top: 400px; width: 132px; height: 132px; font-size: 17px; line-height: 1.15; border-width: 4px; }

  .result-photo { position: absolute; top: 33px; width: 202px; height: 150px; border: 3px solid var(--navy); }
  .result-photo--before { left: 33px; background: linear-gradient(160deg, #a47b6c 0%, #c09080 50%, #7e5e54 100%); }
  .result-photo--after { left: 240px; background: linear-gradient(160deg, #8c5a48 0%, #b06e50 50%, #5e3e34 100%); }
  .result-photo__tag { position: absolute; left: 4px; top: 4px; background: var(--white); color: var(--navy);
    font-family: "Lora", serif; font-weight: 700; font-size: 15px; padding: 2px 6px; }

  .about { position: absolute; left: 28px; top: 216px; width: 228px; font-family: "Lora", serif;
    font-size: 14.5px; line-height: 1.35; color: var(--ink); }
  .about strong { font-weight: 700; }
  .about__services { color: var(--accent); }

  .reasons { position: absolute; left: 278px; top: 216px; width: 170px; font-family: "Lora", serif;
    font-size: 14.5px; line-height: 1.4; color: var(--ink); }
  .reasons__title { color: var(--accent); font-size: 15px; letter-spacing: 0.3px; margin-bottom: 2px; }
  .reasons ul { list-style: none; }
  .reasons li { position: relative; padding-left: 26px; }
  .reasons li::before { content: ""; position: absolute; left: 4px; top: 8px; width: 5px; height: 5px;
    border-radius: 50%; background: var(--ink); }

  .cta { position: absolute; left: 170px; top: 416px; font-family: "Lora", serif; color: var(--navy); }
  .cta__line { font-size: 25px; line-height: 1.3; }
  .cta__phone { font-size: 25px; font-weight: 700; margin-top: 12px; }

  .return-address { position: absolute; left: 542px; top: 38px; font-family: "Montserrat", sans-serif;
    font-size: 11.5px; line-height: 1.55; color: var(--ink); }
  .address-line { position: absolute; left: 540px; width: 336px; border-top: 1.5px dashed var(--rule); }
</style>
</head>
<body>
<main class="canvas">

  <section class="card card--front">
    <div class="kitchen-photo" role="img" aria-label="Photo of a luxury kitchen with polished granite countertops, wood cabinets and a chrome faucet"></div>
    <svg class="wave" viewBox="0 0 870 260" preserveAspectRatio="none" aria-hidden="true">
      <defs>
        <linearGradient id="bandFill" x1="0" y1="0" x2="0" y2="1">
          <stop offset="0" stop-color="#0f5a90"/>
          <stop offset="1" stop-color="#073a63"/>
        </linearGradient>
      </defs>
      <path d="M0 90 C 200 60 300 150 480 110 C 640 75 760 20 870 30 L 870 260 L 0 260 Z" fill="url(#bandFill)"/>
      <path d="M0 90 C 200 60 300 150 480 110 C 640 75 760 20 870 30" fill="none" stroke="#ffffff" stroke-width="3"/>
    </svg>

    <div class="featured">
      <span class="featured__label">AS SEEN ON</span>
      <span class="featured__name">HomeView TV</span>
    </div>

    <div class="brand-seal brand-seal--front">Bright<br>Harbor Co</div>

    <div class="front-contact">
      <p class="front-contact__phone">520.555.0148</p>
      <p class="front-contact__web">www.<span>brightharbor</span>stone.example</p>
      <h1 class="front-contact__headline">Quality Granite &amp; Stone Sealing in Tucson, AZ</h1>
      <p class="front-contact__tagline">We offer top quality services and competitive pricing!</p>
    </div>
  </section>

  <section class="card card--back">
    <div class="result-photo result-photo--before" role="img" aria-label="Dull stone tile floor before cleaning and sealing">
      <span class="result-photo__tag">BEFORE</span>
    </div>
    <div class="result-photo result-photo--after" role="img" aria-label="Glossy restored stone tile floor after cleaning and sealing">
      <span class="result-photo__tag">AFTER</span>
    </div>

    <p class="about">We are a small, <strong>family-owned business</strong>, so you can have full confidence that you will receive <strong>friendly, personalized service</strong> when you work with us! <span class="about__services">We offer stone cleaning and sealing, surface restoration, tile or grout services, and more.</span></p>

    <div class="reasons">
      <h2 class="reasons__title">WHY CHOOSE US</h2>
      <ul>
        <li>As Seen on HomeView TV</li>
        <li>Trade Guild Accredited</li>
        <li>Family Owned and Operated</li>
        <li>One Time Process!</li>
        <li>Lifetime Warranty Against Staining</li>
      </ul>
    </div>

    <div class="brand-seal brand-seal--back">Bright<br>Harbor Co</div>

    <div class="cta">
      <p class="cta__line">Request a free estimate,<br>give us a call today!</p>
      <p class="cta__phone">520.555.0148</p>
    </div>

    <address class="return-address" style="font-style: normal;">
      1180 W Canyon Mesa Rd<br>Suite 210<br>Tucson, AZ 85704
    </address>

    <div class="address-line" style="top: 272px;"></div>
    <div class="address-line" style="top: 332px;"></div>
    <div class="address-line" style="top: 392px;"></div>
  </section>

</main>
</body>
</html>
```